The Marrowfield Hotel Flyer

it is for a Pub that has been in the area for a long time but now we have changed the name and taken over as new owners and now have to try to get all the locals back, eating and drinking..

This Flyer is to try get all the locals to come try the new Marrowfield Hotel.

We have a great new menu with daily food deals
Craft beers
Week nights Live music
Tuesday Comedy night
Sunday live music

Industry/Entity Type

Hotel

```html
<!DOCTYPE html>
<html lang="en">
<head>
<meta charset="utf-8">
<title>The Marrowfield Hotel Flyer</title>
<link href="https://fonts.googleapis.com/css2?family=Arimo:wght@400;700&family=Anton&display=swap" rel="stylesheet">
<style>
  :root {
    --navy: #1a2878;
    --ribbon: #2f3f93;
    --ribbon-tail: #1c2a7c;
    --ribbon-fold: #121c5a;
    --badge: #34449a;
    --glass-light: #ffffff;
    --glass-mid: #eef0f1;
    --glass-edge: #d3d7da;
    --white: #ffffff;
  }
  html, body { margin: 0; padding: 0; overflow: hidden; }
  body { width: 848px; height: 1200px; background: var(--white); }
  .flyer {
    position: relative; width: 848px; height: 1200px; overflow: hidden;
    font-family: "Arimo", Arial, sans-serif; color: var(--navy);
  }
  .glass-backdrop {
    position: absolute; inset: 0;
    background: linear-gradient(90deg, var(--glass-edge) 0%, var(--glass-mid) 6%, var(--glass-light) 18%, var(--glass-light) 82%, var(--glass-mid) 94%, var(--glass-edge) 100%);
  }
  .centered { position: absolute; left: 0; width: 100%; text-align: center; margin: 0; }
  .brand { position: absolute; left: 0; top: 70px; width: 848px; height: 260px; margin: 0; }
  .brand svg { display: block; }
  .invite { width: 700px; }
  .invite-lead { top: 358px; font-size: 40px; }
  .invite-feature {
    font-family: "Anton", Impact, sans-serif; font-size: 66px; letter-spacing: 1px;
    text-shadow: 2px 3px 3px rgba(0,0,0,0.35); line-height: 1.1;
  }
  .feature-menu { top: 410px; }
  .invite-and { top: 500px; font-size: 38px; }
  .feature-beers { top: 552px; }
  .deal-badge { position: absolute; left: 536px; top: 455px; width: 244px; height: 244px; }
  .schedule-day { font-size: 46px; }
  .day-weeknights { top: 700px; }
  .day-tuesday { top: 908px; font-size: 44px; }
  .event-ribbon { position: absolute; left: 118px; width: 600px; height: 115px; }
  .ribbon-music { top: 782px; }
  .ribbon-comedy { top: 980px; }
  .event-title {
    position: absolute; left: 0; width: 100%; text-align: center; top: -4px;
    font-family: "Anton", Impact, sans-serif; font-size: 76px; color: var(--white);
    text-shadow: 2px 3px 2px rgba(0,0,0,0.55), -1px -1px 0 rgba(120,120,120,0.6);
    letter-spacing: 3px; line-height: 1.2; margin: 0;
  }
</style>
</head>
<body>
<main class="flyer">
  <div class="glass-backdrop" role="img" aria-label="Illustration of a clear pint glass behind the flyer content"></div>

  <h1 class="brand" aria-label="The Marrowfield Hotel">
    <svg width="848" height="260" viewBox="0 0 848 260" aria-hidden="true">
      <g fill="var(--navy)" font-family="Arimo, Arial, sans-serif" font-weight="400" text-anchor="middle">
        <text x="424" y="45" font-size="40" letter-spacing="2">THE</text>
        <text x="424" y="195" font-size="190" textLength="680" lengthAdjust="spacingAndGlyphs">MARROWFIELD</text>
        <text x="424" y="242" font-size="40" letter-spacing="2">HOTEL</text>
      </g>
      <g stroke="var(--navy)" stroke-width="3">
        <line x1="85" y1="222" x2="335" y2="222"/>
        <line x1="85" y1="231" x2="335" y2="231"/>
        <line x1="515" y1="222" x2="765" y2="222"/>
        <line x1="515" y1="231" x2="765" y2="231"/>
      </g>
    </svg>
  </h1>

  <p class="centered invite invite-lead">Come try our</p>
  <p class="centered invite invite-feature feature-menu">Great New Menu</p>
  <p class="centered invite invite-and">and</p>
  <p class="centered invite invite-feature feature-beers">Craft Beers</p>

  <svg class="deal-badge" viewBox="0 0 244 244" aria-label="Daily Food Deals">
    <defs>
      <radialGradient id="badgeShade" cx="50%" cy="45%" r="60%">
        <stop offset="0%" stop-color="#6f7cc0"/>
        <stop offset="100%" stop-color="#34449a"/>
      </radialGradient>
    </defs>
    <polygon fill="url(#badgeShade)" stroke="#1c2a7c" stroke-width="2"
      points="122,6 139,37 168,16 172,51 206,44 193,76 228,84 203,108 232,122 203,136 228,160 193,168 206,200 172,193 168,228 139,207 122,238 105,207 76,228 72,193 38,200 51,168 16,160 41,136 12,122 41,108 16,84 51,76 38,44 72,51 76,16 105,37"/>
    <g font-family="Anton, Impact, sans-serif" font-size="40" fill="#ffffff" stroke="#3a3a3a" stroke-width="1.2" text-anchor="middle" letter-spacing="5">
      <text x="124" y="82">Daily</text>
      <text x="124" y="134">Food</text>
      <text x="124" y="186">Deals</text>
    </g>
  </svg>

  <p class="centered schedule-day day-weeknights">Week Nights + Sunday</p>

  <div class="event-ribbon ribbon-music">
    <svg width="600" height="115" viewBox="0 0 600 115" aria-hidden="true">
      <polygon fill="var(--ribbon-tail)" points="0,28 70,28 70,113 0,113 28,70"/>
      <polygon fill="var(--ribbon-tail)" points="600,28 530,28 530,113 600,113 572,70"/>
      <polygon fill="var(--ribbon-fold)" points="57,88 57,113 75,88"/>
      <polygon fill="var(--ribbon-fold)" points="543,88 543,113 525,88"/>
      <rect x="57" y="0" width="486" height="88" fill="var(--ribbon)"/>
    </svg>
    <p class="event-title">Live Music</p>
  </div>

  <p class="centered schedule-day day-tuesday">Tuesday</p>

  <div class="event-ribbon ribbon-comedy">
    <svg width="600" height="115" viewBox="0 0 600 115" aria-hidden="true">
      <polygon fill="var(--ribbon-tail)" points="0,28 70,28 70,113 0,113 28,70"/>
      <polygon fill="var(--ribbon-tail)" points="600,28 530,28 530,113 600,113 572,70"/>
      <polygon fill="var(--ribbon-fold)" points="57,88 57,113 75,88"/>
      <polygon fill="var(--ribbon-fold)" points="543,88 543,113 525,88"/>
      <rect x="57" y="0" width="486" height="88" fill="var(--ribbon)"/>
    </svg>
    <p class="event-title">Comedy Night</p>
  </div>
</main>
</body>
</html>
```